Elegant Business Cards & Letterhead

We will need the following that need to be designed: Letterhead and Business Cards, there winer will be re-hired for the balance of our stationary needs. Text for the cards and letterheads:

- Corporate Card instead of name
- landline: +971 (4) 362 7041
- mobile: +971 56 2819 605
- 800TUTOR
- email: dubai@velmora-lune.com
- www.velmora-lune.com
- PO Box 387261
Address: Castellan Heights Suite 1708, Dubai UAE

Thank you

Target Market(s)

VIPs, HNWI, High-end Families.

Industry/Entity Type

Luxury Market

Font styles to use
Other font styles liked:
• as explained

Colors

Designer to choose only greyscale colors for use in the design.

Requirements
Must have
• Elegant, Simple, Luxurious, Minimalistic
Nice to have
• Luxury, Golds, Engravings,
Should not have
• Much colors, funky,

```html
<!DOCTYPE html>
<html lang="en">
<head>
<meta charset="utf-8">
<title>Velmora Lune – Business Cards</title>
<link rel="stylesheet" href="https://fonts.googleapis.com/css2?family=Marcellus&family=Open+Sans:wght@400;700&display=swap">
<style>
  :root {
    --backdrop: #222222;
    --card-front: #f3f3ec;
    --card-back: #fdfdf4;
    --gold: #d4a326;
    --gold-light: #f1cd45;
    --gold-deep: #b9801f;
    --ink: #111111;
    --white: #ffffff;
  }
  html, body {
    margin: 0;
    padding: 0;
    overflow: hidden;
  }
  body {
    width: 1200px;
    height: 780px;
    background: var(--backdrop);
    position: relative;
    font-family: "Open Sans", Arial, sans-serif;
  }
  .card {
    position: absolute;
    top: 236px;
    width: 540px;
    height: 308px;
    overflow: hidden;
    box-shadow: 0 12px 30px rgba(0,0,0,0.5);
  }
  .card--front { left: 40px; background: var(--card-front); }
  .card--back  { left: 620px; background: var(--card-back); }

  .card__art { position: absolute; inset: 0; }

  .brand-name {
    position: absolute;
    margin: 0;
    font-family: "Marcellus", Georgia, serif;
    font-weight: 400;
    color: var(--gold);
    letter-spacing: 2px;
    white-space: nowrap;
    line-height: 1;
  }
  .card--front .brand-name { left: 190px; top: 30px; font-size: 34px; }
  .card--back .brand-name {
    left: 0; right: 0; top: 131px;
    text-align: center;
    font-size: 46px;
  }

  .card-type {
    position: absolute;
    left: 58px;
    top: 104px;
    margin: 0;
    font-size: 24px;
    font-weight: 700;
    color: var(--gold);
    line-height: 1.1;
    white-space: nowrap;
  }

  .divider {
    position: absolute;
    left: 284px;
    top: 100px;
    width: 1.5px;
    height: 94px;
    background: var(--ink);
  }

  .contacts {
    position: absolute;
    left: 298px;
    top: 100px;
    margin: 0;
    padding: 0;
    list-style: none;
    font-size: 13px;
    color: var(--ink);
  }
  .contacts li {
    display: flex;
    align-items: center;
    gap: 8px;
    height: 19px;
    white-space: nowrap;
  }
  .contacts svg { width: 12px; height: 12px; flex: none; }

  .address {
    position: absolute;
    left: 40px;
    top: 268px;
    margin: 0;
    font-size: 13px;
    color: var(--white);
    letter-spacing: 0.2px;
    white-space: nowrap;
  }
</style>
</head>
<body>

  <section class="card card--front" aria-label="Business card front">
    <svg class="card__art" viewBox="0 0 540 308" aria-hidden="true">
      <defs>
        <linearGradient id="goldBand" x1="0" y1="0" x2="1" y2="1">
          <stop offset="0" stop-color="var(--gold-light)"/>
          <stop offset="0.45" stop-color="var(--gold-deep)"/>
          <stop offset="1" stop-color="var(--gold-light)"/>
        </linearGradient>
      </defs>
      <path class="gold-band" d="M0,118 C60,210 220,250 540,262 L540,308 L0,308 Z" fill="url(#goldBand)"/>
      <path class="sweep-line" d="M22,112 C70,200 230,240 500,256" fill="none" stroke="var(--ink)" stroke-width="2.5" stroke-linecap="round"/>
    </svg>

    <h1 class="brand-name">VELMORA LUNE</h1>

    <p class="card-type">Corporate Card</p>

    <div class="divider"></div>

    <ul class="contacts">
      <li>
        <svg viewBox="0 0 12 12" aria-hidden="true"><circle cx="6" cy="6" r="6" fill="var(--gold)"/><path d="M4 3 L5 3 L5.5 4.5 L4.8 5.2 Q5.6 6.6 6.8 7.2 L7.5 6.5 L9 7 L9 8 Q8.5 9 7.5 9 Q3 8 3 4 Q3 3 4 3Z" fill="var(--white)"/></svg>
        <span>+971 (4) 362 7041</span>
      </li>
      <li>
        <svg viewBox="0 0 12 12" aria-hidden="true"><circle cx="6" cy="6" r="6" fill="var(--gold)"/><rect x="4" y="2.6" width="4" height="6.8" rx="0.8" fill="var(--white)"/><circle cx="6" cy="8.4" r="0.5" fill="var(--gold)"/></svg>
        <span>+971 56 2819 605</span>
      </li>
      <li>
        <svg viewBox="0 0 12 12" aria-hidden="true"><circle cx="6" cy="6" r="6" fill="var(--gold)"/><path d="M4 3 L5 3 L5.5 4.5 L4.8 5.2 Q5.6 6.6 6.8 7.2 L7.5 6.5 L9 7 L9 8 Q8.5 9 7.5 9 Q3 8 3 4 Q3 3 4 3Z" fill="var(--white)"/></svg>
        <span>800TUTOR</span>
      </li>
      <li>
        <svg viewBox="0 0 12 12" aria-hidden="true"><circle cx="6" cy="6" r="6" fill="var(--gold)"/><rect x="3" y="4" width="6" height="4.2" fill="var(--white)"/><path d="M3 4 L6 6.4 L9 4" fill="none" stroke="var(--gold)" stroke-width="0.8"/></svg>
        <span>dubai@velmora-lune.com</span>
      </li>
      <li>
        <svg viewBox="0 0 12 12" aria-hidden="true"><circle cx="6" cy="6" r="6" fill="var(--gold)"/><circle cx="6" cy="6" r="3.2" fill="none" stroke="var(--white)" stroke-width="0.8"/><path d="M2.8 6 H9.2 M6 2.8 Q4.4 6 6 9.2 Q7.6 6 6 2.8" fill="none" stroke="var(--white)" stroke-width="0.7"/></svg>
        <span>www.velmora-lune.com</span>
      </li>
    </ul>

    <p class="address">PO Box 387261 · Castellan Heights Suite 1708, Dubai UAE</p>
  </section>

  <section class="card card--back" aria-label="Business card back">
    <h2 class="brand-name">VELMORA LUNE</h2>
  </section>

</body>
</html>
```